Finiding oppertunites in Real Estate 6.15.20

size of ad 7” x 9.6”
1-I like the ad to stand out and attract people's attention.
2-you should be able to see the text of the ad clearly .. see the attachment anything in yellow is instructions.
3-the list of topics should not be the main part of the ad
4-if you decide you want a picture or vector of a person .. (you decide)
then it should be a white male about 25-30 years old wearing a solid white or blue shirt and not long hair.
5-leave 1 inch for footer
see attachment
Good luck

Target Market(s)

potential male students 25-35 years of age

Industry/Entity Type

Education

Requirements
Must have
• will stand out and people would want to see it.
should be able to read the words of ad
Nice to have
• how to make money in real estate on one line

```html
<!DOCTYPE html>
<html lang="en">
<head>
<meta charset="utf-8">
<title>Real Estate Career Course Flyer</title>
<link rel="stylesheet" href="https://fonts.googleapis.com/css2?family=League+Gothic&family=Oswald:wght@500;600;700&family=Roboto+Condensed:wght@400&display=swap">
<style>
  :root {
    --yellow: #f9b000;
    --blue: #0041a8;
    --blue-deep: #003287;
    --ink: #262626;
    --red: #dd0000;
    --band-grey: #efefef;
    --paper: #ffffff;
    --backdrop: #5a5a5a;
    --edge-grey: #ececec;
  }
  * { margin: 0; padding: 0; box-sizing: border-box; }
  html, body { width: 938px; height: 1200px; overflow: hidden; background: var(--backdrop); }
  .flyer {
    position: absolute; left: 31px; top: 0;
    width: 876px; height: 1200px;
    background: var(--paper);
    overflow: hidden;
    font-family: "Oswald", sans-serif;
  }
  .hero-art { position: absolute; left: 0; top: 0; width: 420px; height: 1080px; }
  .abs { position: absolute; white-space: nowrap; line-height: 1; }
  .title-top {
    right: 28px; top: 44px;
    font-family: "League Gothic", sans-serif; font-size: 108px; color: var(--yellow);
  }
  .title-main {
    right: 28px; top: 134px;
    font-family: "League Gothic", sans-serif; font-size: 112px; color: var(--blue);
  }
  .tagline-band {
    position: absolute; left: 0; top: 246px; width: 876px; height: 55px;
  }
  .tagline {
    right: 35px; top: 253px;
    font-family: "League Gothic", sans-serif; font-size: 44px; color: var(--yellow);
  }
  .audience {
    right: 36px; top: 336px; text-align: right;
    font-weight: 500; font-size: 29px; line-height: 38px; color: var(--blue);
  }
  .pitch {
    right: 45px; top: 435px; text-align: right;
    font-weight: 600; font-size: 52px; line-height: 51px; letter-spacing: -1px;
    color: var(--yellow);
  }
  .pitch .lead { color: var(--ink); }
  .date-band {
    position: absolute; left: 399px; top: 687px; width: 477px; height: 131px;
    background: var(--band-grey);
  }
  .session-band {
    position: absolute; left: 410px; top: 633px; width: 466px; height: 54px;
    background: var(--red);
  }
  .session-text {
    left: 410px; width: 466px; top: 637px; text-align: center;
    font-weight: 600; font-size: 41px; color: #fff;
  }
  .start-label {
    left: 410px; width: 466px; top: 690px; text-align: center;
    font-weight: 600; font-size: 38px; color: var(--ink);
  }
  .start-date {
    left: 410px; width: 466px; top: 722px; text-align: center;
    font-weight: 700; font-size: 90px; letter-spacing: -1px; color: var(--ink);
  }
  .badge { position: absolute; left: 214px; top: 605px; width: 240px; height: 240px; }
  .badge-text {
    position: absolute; left: 214px; top: 605px; width: 240px; height: 240px;
    display: flex; flex-direction: column; align-items: center; justify-content: center;
    transform: rotate(-9deg);
    font-family: "League Gothic", sans-serif; color: #fff; font-size: 60px; line-height: 50px;
    text-shadow: 0 2px 2px rgba(0,0,0,.35);
  }
  .topics-title {
    left: 455px; top: 846px;
    font-weight: 500; font-size: 22px; color: var(--blue);
  }
  .topics {
    position: absolute; top: 879px; list-style: none;
    font-family: "Roboto Condensed", sans-serif; font-size: 18.5px; line-height: 25.4px; color: var(--ink);
  }
  .topics li { position: relative; padding-left: 19px; white-space: nowrap; }
  .topics li::before {
    content: ""; position: absolute; left: 0; top: 10px;
    width: 6px; height: 6px; border-radius: 50%; background: var(--yellow);
  }
  .topics-left { left: 455px; }
  .topics-right { left: 673px; }
</style>
</head>
<body>
<div class="flyer">
  <svg class="hero-art" viewBox="0 0 420 1080" role="img" aria-label="Illustration: young man in a white shirt and grey trousers holding a laptop, set against a yellow sunburst">
    <path d="M0 0 H250 C330 60 330 250 250 470 C215 560 205 640 250 760 C300 860 425 900 395 1078 H0 Z" fill="var(--edge-grey)"/>
    <path d="M0 0 H236 C312 60 312 250 236 470 C201 560 191 640 236 760 C286 860 408 900 378 1078 H0 Z" fill="var(--yellow)"/>
  </svg>

  <div class="abs title-top">REAL ESTATE</div>
  <div class="abs title-main">CAREER COURSE</div>

  <svg class="tagline-band" viewBox="0 0 876 55" aria-hidden="true">
    <polygon points="296,0 876,0 876,55 275,55" fill="var(--ink)"/>
  </svg>
  <div class="abs tagline">How to Make Money In In Real Estate?</div>

  <div class="abs audience">For those who have started or<br>would like to go into Real Estate</div>

  <div class="abs pitch"><span class="lead">AN INVESTMENT IN</span><br>KNOWLEDGE OPENS UP<br>UNTOLD OPPORTUNITIE</div>

  <div class="date-band"></div>
  <div class="session-band"></div>
  <div class="abs session-text">12 SESSION COURSE</div>
  <div class="abs start-label">CLASSES STARTING</div>
  <div class="abs start-date">JUNE 16</div>

  <svg class="badge" viewBox="-120 -120 240 240" aria-hidden="true">
    <defs>
      <linearGradient id="badgeFill" x1="0" y1="0" x2="1" y2="1">
        <stop offset="0" stop-color="#1456c4"/>
        <stop offset="1" stop-color="var(--blue-deep)"/>
      </linearGradient>
    </defs>
    <g fill="#ffffff">
      <rect x="-84" y="-84" width="168" height="168" transform="rotate(0)"/>
      <rect x="-84" y="-84" width="168" height="168" transform="rotate(15)"/>
      <rect x="-84" y="-84" width="168" height="168" transform="rotate(30)"/>
      <rect x="-84" y="-84" width="168" height="168" transform="rotate(45)"/>
      <rect x="-84" y="-84" width="168" height="168" transform="rotate(60)"/>
      <rect x="-84" y="-84" width="168" height="168" transform="rotate(75)"/>
    </g>
    <g fill="url(#badgeFill)">
      <rect x="-76" y="-76" width="152" height="152" transform="rotate(0)"/>
      <rect x="-76" y="-76" width="152" height="152" transform="rotate(15)"/>
      <rect x="-76" y="-76" width="152" height="152" transform="rotate(30)"/>
      <rect x="-76" y="-76" width="152" height="152" transform="rotate(45)"/>
      <rect x="-76" y="-76" width="152" height="152" transform="rotate(60)"/>
      <rect x="-76" y="-76" width="152" height="152" transform="rotate(75)"/>
    </g>
  </svg>
  <div class="badge-text"><span>REMOTE</span><span>SESSIONS</span></div>

  <div class="abs topics-title">A PARTIAL LISTING OF TOPICS :</div>
  <ul class="topics topics-left">
    <li>Single-family</li>
    <li>Multifamily</li>
    <li>Management</li>
    <li>Real Estate Concepts</li>
    <li>Real Estate law</li>
    <li>Investment properties</li>
    <li>Foreclosures</li>
  </ul>
  <ul class="topics topics-right">
    <li>Rehab</li>
    <li>Foreclosures</li>
    <li>Short sales</li>
    <li>Development</li>
    <li>Finical modeling</li>
    <li>HUD properties</li>
    <li>Due Diligencee</li>
  </ul>
</div>
</body>
</html>
```